Calvanta Group Real Estate Company business cards

New business card design, we are generally happy with the basic layout of the existing front of business card, (feel free to change) but require a head shot photo on the back side.

http://www.calvanta.com.au/

Attached logos, and existing business card

------------------------------

Target Market(s)

Real estate

Industry/Entity Type

Real Estate

Contact Information for Business Card

Standard size double sided

Font styles to use
Other font styles liked:
• Futura

Requirements
Must have
• Photo head shot on the back side
Nice to have
• yes
Should not have
• No

```html
<!DOCTYPE html>
<html lang="en">
<head>
<meta charset="utf-8">
<title>Calvanta Group – Business Cards</title>
<link rel="stylesheet" href="https://fonts.googleapis.com/css2?family=Jost:wght@400;500;700;800&display=swap">
<style>
  :root {
    --backdrop: #2e2e30;
    --brand-purple: #2e2160;
    --brand-orange: #f39a1e;
    --paper: #ffffff;
    --ink-grey: #8a8a96;
    --photo-tone-a: #e9eaee;
    --photo-tone-b: #c9ccd6;
  }
  * { box-sizing: border-box; margin: 0; padding: 0; }
  html, body {
    width: 1200px; height: 900px; overflow: hidden;
    background: var(--backdrop);
    font-family: "Jost", "Futura", sans-serif;
  }
  .sheet { position: relative; width: 1200px; height: 900px; }
  .card {
    position: absolute; left: 320px;
    width: 560px; height: 320px;
    box-shadow: 0 18px 40px rgba(0,0,0,0.45);
    overflow: hidden;
  }

  /* Brand lock-up: name with small group line aligned under its right edge */
  .brand-lockup { display: inline-flex; flex-direction: column; align-items: stretch; }
  .wordmark { font-weight: 500; letter-spacing: -1px; line-height: 1; }
  .wordmark-sub {
    font-size: 11px; letter-spacing: 8px; color: var(--ink-grey);
    text-align: right; text-transform: uppercase; line-height: 1; margin-top: 4px;
  }

  /* Front */
  .card--front {
    top: 90px;
    background: var(--brand-purple);
    color: var(--paper);
    display: flex; flex-direction: column; align-items: center; justify-content: center;
  }
  .card--front .wordmark { font-size: 82px; color: var(--paper); }
  .services { margin-top: 18px; font-size: 18px; font-weight: 500; letter-spacing: 2px; }
  .services .divider { color: var(--brand-orange); margin: 0 6px; }
  .front-web { margin-top: 10px; font-size: 18px; font-weight: 700; letter-spacing: 1px; }
  .accent { color: var(--brand-orange); }

  /* Back */
  .card--back { top: 490px; background: var(--paper); color: var(--brand-purple); }
  .side-band {
    position: absolute; top: 0; bottom: 0; left: 20px; width: 42px;
    background: var(--brand-purple);
  }
  .back-brand { position: absolute; left: 92px; top: 30px; }
  .card--back .wordmark { font-size: 58px; color: var(--brand-purple); }
  .card--back .wordmark-sub { font-size: 9px; letter-spacing: 7px; margin-top: 3px; }
  .tagline { margin-top: 6px; font-size: 19px; line-height: 1.2; color: var(--brand-purple); }
  .agent { position: absolute; left: 92px; top: 156px; }
  .agent-name {
    font-size: 24px; font-weight: 800; letter-spacing: 0.5px;
    text-transform: uppercase; line-height: 1.15;
  }
  .agent-role {
    font-size: 13px; color: var(--brand-orange); text-transform: uppercase;
    letter-spacing: 0.5px; line-height: 1.4;
  }
  .abn { font-size: 13px; line-height: 1.4; }
  .abn-label { color: var(--brand-orange); }
  .contact-list { list-style: none; margin-top: 6px; }
  .contact-list li {
    display: flex; align-items: center; gap: 8px; font-size: 13px; line-height: 1.45;
  }
  .contact-list svg { width: 12px; height: 12px; flex: none; }
  .headshot {
    position: absolute; right: 40px; top: 40px;
    width: 170px; height: 170px; border-radius: 50%;
    border: 2px solid var(--brand-purple);
    background: radial-gradient(circle at 45% 40%, var(--photo-tone-a), var(--photo-tone-b));
  }
</style>
</head>
<body>
<main class="sheet">

  <section class="card card--front" aria-label="Business card front">
    <div class="brand-lockup">
      <div class="wordmark">calvanta</div>
      <div class="wordmark-sub">Group</div>
    </div>
    <div class="services">Buy<span class="divider">|</span>Sell<span class="divider">|</span>Rent</div>
    <div class="front-web"><span class="accent">www.</span>calvanta.com<span class="accent">.au</span></div>
  </section>

  <section class="card card--back" aria-label="Business card back">
    <div class="side-band"></div>

    <div class="back-brand">
      <div class="brand-lockup">
        <div class="wordmark">calvanta</div>
        <div class="wordmark-sub">Group</div>
      </div>
      <div class="tagline">let us find you a home</div>
    </div>

    <div class="agent">
      <div class="agent-name">Daniel Tran</div>
      <div class="agent-role">Director</div>
      <div class="abn"><span class="abn-label">ABN:</span> 51 824 603 197</div>
      <ul class="contact-list">
        <li>
          <svg viewBox="0 0 12 12" aria-hidden="true"><rect x="3" y="1" width="6" height="10" rx="1" fill="none" stroke="var(--brand-orange)" stroke-width="1.3"/><circle cx="6" cy="9" r="0.7" fill="var(--brand-orange)"/></svg>
          0412 555 318
        </li>
        <li>
          <svg viewBox="0 0 12 12" aria-hidden="true"><rect x="1" y="2.5" width="10" height="7" fill="none" stroke="var(--brand-orange)" stroke-width="1.3"/><path d="M1 2.5 L6 6.5 L11 2.5" fill="none" stroke="var(--brand-orange)" stroke-width="1.3"/></svg>
          daniel.tran@calvanta.com.au
        </li>
        <li>
          <svg viewBox="0 0 12 12" aria-hidden="true"><circle cx="6" cy="6" r="5" fill="none" stroke="var(--brand-orange)" stroke-width="1.2"/><ellipse cx="6" cy="6" rx="2.2" ry="5" fill="none" stroke="var(--brand-orange)" stroke-width="1"/><line x1="1" y1="6" x2="11" y2="6" stroke="var(--brand-orange)" stroke-width="1"/></svg>
          www.calvanta.com.au
        </li>
      </ul>
    </div>

    <div class="headshot" role="img" aria-label="Head shot photo of the agent"></div>
  </section>

</main>
</body>
</html>
```